Lumeno-Interior design firm
Hello all,
I will announce the winner in the next few hours...
I appreciate your AMAZING ideas and all the many revisions that each of you submited, they helped us to understand your creative proposals and at the end to select a winner.
THANK YOU!
Lumeno Design
Draft #317 and #318
We are looking at some winning designs already and we will send our efforts towards those. i appreciate your entry very much.
Thanks!
Draft #312
The font on the subject LUMENO Interior design firm needs to be changed. I dont like it. I like the font used on the HOME, PORTFOLIO, etc...main subjects if that helps!
Everything else looks amazing!
hi all,
I had an unexpected business to attend today and I was not able to complete the feedback to all of you. We decided to extend the time to provide the missing feedback...I will provide to all, just give me some time.
I have decided to extend the contest. This was a last minute descision.
I appreciate your entry but is not what I am looking for. I don't want to waste your time as well as I prefer to concentrate on the designs/designers that have invested some time with me already.
Thank you and I appreciate your understanding!
Thanks brightquill! I really appreciate your understanding!
Draft #273
Can you justified all the texts used on each page? That will be great for final review.
Drafts #270 and #272
the text needs to be justified and that will make it!
Draft #269
HOME
There is a small misspell at the bottom left...it reads Lemeno instead of Lumeno.
Ater that revision you are set!
@PH, Thanks for your comments...
Dear Brightquill,
I like your entry but i am sorry to say that there is nothing original about it. I feel respect for everyones work and even when I am not an expert I feel you are copying other entries. I can not give you credit for someone else's ideas and I would appreciate if you come up with the same concept but with something that is your very own creation.
With all my respect...
Draft #251
Looks good just to revise the "yellow" cubes to be softer...and also please use my pictures for each page so I can compare with everyone else.
Thank you so much!
Draft #250
I would prefer to container the ABOUT US description on within the limits of the cubes so if necessary lets remove the "yellow" cubes so we can move up the wording and fit it within...
Use the service wording as reference...it is contained and it does not go below the "cubes"
Draft #249
lets list the services on a horizontal way inside the "cubes" Makes sense? linear way showing the services and the main wording as is.
Draft #248
can we made the windows with tabs LIVING, DINING, BEDROOM ACCENTS and KIDS to be one of the "cubes" from your design?
maybe using the bottom five...?
then when you click on I would like to see a complete picture...hopefully you come up with an idea but if not we can look at it together after revision...
Thanks
Draft #247
My only change is the "yellow" buttons to be more with softer colors...soft grey/white...or any suggestions within my request.
Draft #234
Wording needs to be consistent...I prefer white please revise.
Draft #227
Revisions:
I dont like the phone image under phone, please remove
Please do not underline the website
I prefer just letter on the front:
P: for phone
W: for website
etc...
In your case I would prefer not to use my picture...lets just remove it and after all this it should be done!
Looking good!
Draft #223
I need you to add the wording that I sent for services as well...it is important!
Thanks! Everything else looks perfect!
Hello@PH
I`m just waiting for your Feedback on
#221(Home page), #222(Portfolio Page), #223(Services Page),#224(About Us Page), & #225(Contact Page)
Zora
FOR EVERYONE:
PLEASE submit your complete designs, I wont be extending the project and with the time left I wont be able to give feedback and revisions to detail to everyone.
I really appreciate your hard work on attention to my project.
You ALL are very talented!
Good luck!
Draft #208 you can move forward with the inner pages.
Draft #207
I need the text to be justified please. You can complete your design with all he pages, I like the layout as is.
Look forward to final entries.

```html
<!DOCTYPE html>
<html lang="en">
<head>
<meta charset="utf-8">
<title>Lumeno – Interior Design Firm</title>
<link rel="stylesheet" href="https://fonts.googleapis.com/css2?family=Questrial&family=Open+Sans:wght@400;600&display=swap">
<style>
  :root{
    --page-bg:#f3f3f3;
    --page-bg-soft:#ffffff;
    --brand-gold:#b59d5e;
    --text-dark:#555555;
    --text-body:#7a7a7a;
    --text-muted:#8c8c8c;
    --nav-bar:#e4e4e4;
    --nav-bar-light:#f4f4f4;
    --accent-orange:#e8901f;
    --footer-bg:#e2e2e2;
    --footer-line:#cfcfcf;
    --social-blue:#3b6aa8;
  }
  html,body{margin:0;padding:0;overflow:hidden;}
  body{
    width:1200px;height:732px;position:relative;
    background:linear-gradient(180deg,var(--page-bg-soft) 0%,var(--page-bg) 100%);
    font-family:"Open Sans",Arial,sans-serif;
  }
  .brand{position:absolute;left:144px;top:30px;display:flex;align-items:flex-start;}
  .brand-dot{width:84px;height:84px;border-radius:50%;background:#e9e2cf;margin-right:60px;margin-top:6px;}
  .brand-name{
    font-family:"Questrial",sans-serif;font-size:60px;line-height:60px;
    letter-spacing:6px;color:var(--brand-gold);margin:0;font-weight:400;
  }
  .brand-tagline{
    font-family:"Questrial",sans-serif;font-size:17px;color:var(--text-muted);
    margin:6px 0 0 2px;letter-spacing:0.5px;
  }
  .main-nav{position:absolute;left:142px;top:138px;width:150px;}
  .main-nav a{
    display:block;height:24px;line-height:24px;margin-bottom:5px;text-align:center;
    font-size:13px;color:var(--text-muted);text-decoration:none;
    background:linear-gradient(90deg,var(--nav-bar-light),var(--nav-bar) 50%,var(--nav-bar-light));
  }
  .main-nav a.is-current{color:var(--text-dark);font-weight:600;}
  .mosaic{position:absolute;left:0;top:0;}
  .welcome{position:absolute;left:140px;top:480px;width:260px;}
  .welcome-title{font-family:"Questrial",sans-serif;font-size:22px;color:var(--text-dark);margin:0 0 10px;font-weight:400;}
  .welcome-text{font-size:12px;line-height:17px;color:var(--text-body);text-align:justify;margin:0;}
  .read-more{display:inline-block;margin-top:10px;font-size:12px;color:var(--accent-orange);text-decoration:none;}
  .site-footer{
    position:absolute;left:0;top:667px;width:1200px;height:65px;
    background:var(--footer-bg);border-top:1px solid var(--footer-line);
  }
  .copyright{position:absolute;left:140px;top:12px;margin:0;font-size:11px;color:var(--text-body);}
  .footer-nav{position:absolute;left:140px;top:30px;font-size:11px;color:var(--text-body);}
  .footer-nav a{color:var(--text-body);text-decoration:none;margin-right:6px;}
  .footer-nav span{margin-right:6px;}
  .follow{position:absolute;left:852px;top:16px;display:flex;align-items:center;}
  .follow-label{font-family:"Questrial",sans-serif;font-size:17px;color:var(--text-dark);margin-right:16px;}
  .social-square{width:24px;height:24px;border-radius:4px;background:var(--social-blue);margin-right:14px;}
</style>
</head>
<body>

<header class="brand">
  <div class="brand-dot"></div>
  <div>
    <h1 class="brand-name">LUMENO</h1>
    <p class="brand-tagline">Interior Design • Architecture • Art</p>
  </div>
</header>

<nav class="main-nav">
  <a href="#" class="is-current">Home</a>
  <a href="#">Portfolio</a>
  <a href="#">Services</a>
  <a href="#">About Us</a>
  <a href="#">Contact</a>
</nav>

<svg class="mosaic" width="1200" height="667" viewBox="0 0 1200 667">
  <defs>
    <linearGradient id="roomTone" gradientUnits="userSpaceOnUse" x1="404" y1="29" x2="1020" y2="645">
      <stop offset="0" stop-color="#f1ece3"/>
      <stop offset="0.4" stop-color="#ddd3c3"/>
      <stop offset="0.7" stop-color="#9a8063"/>
      <stop offset="1" stop-color="#5a4331"/>
    </linearGradient>
    <linearGradient id="plantTone" x1="0" y1="0" x2="1" y2="1">
      <stop offset="0" stop-color="#7e9a5a"/>
      <stop offset="1" stop-color="#3f5a2c"/>
    </linearGradient>
    <linearGradient id="orangeTone" x1="0" y1="0" x2="0" y2="1">
      <stop offset="0" stop-color="#f5ad45"/>
      <stop offset="1" stop-color="#e08418"/>
    </linearGradient>
  </defs>

  <g class="photo-tiles" role="img" aria-label="Photograph of a bright dining room with an arched doorway, table lamps, candlesticks and upholstered chairs" fill="url(#roomTone)">
    <rect x="580" y="29" width="86" height="86" rx="8"/>
    <rect x="668" y="29" width="86" height="86" rx="8"/>
    <rect x="756" y="29" width="86" height="86" rx="8"/>
    <rect x="844" y="29" width="86" height="86" rx="8"/>

    <rect x="404" y="117" width="86" height="86" rx="8"/>
    <rect x="492" y="117" width="86" height="86" rx="8"/>
    <rect x="580" y="117" width="86" height="86" rx="8"/>
    <rect x="668" y="117" width="86" height="86" rx="8"/>
    <rect x="756" y="117" width="86" height="86" rx="8"/>
    <rect x="844" y="117" width="86" height="86" rx="8"/>
    <rect x="932" y="117" width="86" height="86" rx="8"/>

    <rect x="404" y="205" width="86" height="86" rx="8"/>
    <rect x="492" y="205" width="86" height="86" rx="8"/>
    <rect x="580" y="205" width="86" height="86" rx="8"/>
    <rect x="668" y="205" width="86" height="86" rx="8"/>
    <rect x="756" y="205" width="86" height="86" rx="8"/>
    <rect x="844" y="205" width="86" height="86" rx="8"/>
    <rect x="932" y="205" width="86" height="86" rx="8"/>

    <rect x="228" y="293" width="86" height="86" rx="8" fill="url(#plantTone)"/>
    <rect x="316" y="293" width="86" height="86" rx="8" fill="url(#plantTone)"/>
    <rect x="404" y="293" width="86" height="86" rx="8"/>
    <rect x="492" y="293" width="86" height="86" rx="8"/>
    <rect x="580" y="293" width="86" height="86" rx="8"/>
    <rect x="668" y="293" width="86" height="86" rx="8"/>
    <rect x="756" y="293" width="86" height="86" rx="8"/>
    <rect x="844" y="293" width="86" height="86" rx="8"/>
    <rect x="932" y="293" width="86" height="86" rx="8"/>

    <rect x="404" y="381" width="86" height="86" rx="8"/>
    <rect x="492" y="381" width="86" height="86" rx="8"/>
    <rect x="580" y="381" width="86" height="86" rx="8"/>
    <rect x="668" y="381" width="86" height="86" rx="8"/>
    <rect x="756" y="381" width="86" height="86" rx="8"/>
    <rect x="844" y="381" width="86" height="86" rx="8"/>
    <rect x="932" y="381" width="86" height="86" rx="8"/>

    <rect x="404" y="469" width="86" height="86" rx="8"/>
    <rect x="492" y="469" width="86" height="86" rx="8"/>
    <rect x="580" y="469" width="86" height="86" rx="8"/>
    <rect x="668" y="469" width="86" height="86" rx="8"/>
    <rect x="756" y="469" width="86" height="86" rx="8"/>
    <rect x="844" y="469" width="86" height="86" rx="8"/>
    <rect x="932" y="469" width="86" height="86" rx="8"/>

    <rect x="492" y="557" width="86" height="86" rx="8"/>
    <rect x="580" y="557" width="86" height="86" rx="8"/>
    <rect x="668" y="557" width="86" height="86" rx="8"/>
    <rect x="756" y="557" width="86" height="86" rx="8"/>
    <rect x="844" y="557" width="86" height="86" rx="8"/>
  </g>

  <g class="contact-tiles">
    <rect x="140" y="381" width="86" height="86" rx="8" fill="url(#orangeTone)"/>
    <text x="183" y="440" text-anchor="middle" font-family="Georgia, serif" font-weight="bold" font-size="42" fill="#ffffff">i</text>

    <rect x="228" y="381" width="86" height="86" rx="8" fill="url(#orangeTone)"/>
    <text x="271" y="437" text-anchor="middle" font-family="Arial, sans-serif" font-weight="bold" font-size="36" fill="#ffffff">@</text>

    <rect x="316" y="381" width="86" height="86" rx="8" fill="url(#orangeTone)"/>
    <path d="M346 407 q-4 4 0 14 q8 18 24 26 q8 3 12 -1 l3 -4 q1 -2 -1 -4 l-8 -6 q-2 -1 -4 1 l-3 3 q-9 -4 -14 -14 l3 -3 q2 -2 1 -4 l-5 -8 q-2 -2 -4 -1 z" fill="#ffffff"/>
  </g>
</svg>

<section class="welcome">
  <h2 class="welcome-title">Welcome To LUMENO</h2>
  <p class="welcome-text">We are interior design firm with several years practice founded 7 established in the Cedarbrook,Ohio. Our goal is to provide a superb experience to our clients under the guidance of our founder Architect Elena Varga and her extraordinary eye on design.</p>
  <a href="#" class="read-more">» Read More...</a>
</section>

<footer class="site-footer">
  <p class="copyright">Copyright © 2011 LUMENO - Interior Design Firm. All Rights Reserved.</p>
  <nav class="footer-nav">
    <a href="#">Home</a><span>|</span>
    <a href="#">Services</a><span>|</span>
    <a href="#">About Us</a><span>|</span>
    <a href="#">Contact</a>
  </nav>
  <div class="follow">
    <span class="follow-label">Follow Us:</span>
    <span class="social-square"></span>
    <span class="social-square"></span>
    <span class="social-square"></span>
  </div>
</footer>

</body>
</html>
```